Business Card Design

I give lessons and clinics for dressage riders
I would like the design to be an outline (with broad lines) of a dressage horse and rider with in background of whole card with print over top tan or parchment card with burgundy print

Industry/Entity Type

Business

Contact Information for Business Card

Tod Harlick
555-317-0492
Classical dressage training for the modern American
Clinics, lessons, training level -Prix St. George

Requirements
Must have
• broad lined outline of dressage horse and rider

```html
<!DOCTYPE html>
<html lang="en">
<head>
<meta charset="utf-8">
<title>Tod Harlick – Dressage Training Card</title>
<link href="https://fonts.googleapis.com/css2?family=Cormorant+SC:wght@500&family=Cormorant+Garamond:ital,wght@0,500;1,500&display=swap" rel="stylesheet">
<style>
  :root {
    --burgundy: #8b1a40;
    --burgundy-soft: #9a2a50;
    --parchment: #f5e8bd;
  }
  html, body {
    margin: 0;
    padding: 0;
    overflow: hidden;
    background: var(--parchment);
  }
  .card {
    position: relative;
    width: 702px;
    height: 1200px;
    overflow: hidden;
    background: var(--parchment);
  }
  .card__backdrop {
    position: absolute;
    inset: 0;
    width: 702px;
    height: 1200px;
  }
  .card__text {
    position: absolute;
    left: 75px;
    right: 30px;
    color: var(--burgundy);
    margin: 0;
  }
  .card__name {
    top: 596px;
    font-family: "Cormorant SC", "Times New Roman", serif;
    font-weight: 500;
    font-size: 74px;
    line-height: 90px;
    letter-spacing: 1px;
  }
  .card__phone {
    top: 704px;
    font-family: "Cormorant Garamond", "Times New Roman", serif;
    font-weight: 500;
    font-size: 62px;
    line-height: 80px;
    letter-spacing: 7px;
  }
  .card__services {
    top: 794px;
    font-family: "Cormorant Garamond", "Times New Roman", serif;
    font-style: italic;
    font-weight: 500;
    font-size: 42px;
    line-height: 66.5px;
    letter-spacing: 0.2px;
  }
  .card__services span {
    display: block;
    white-space: nowrap;
  }
</style>
</head>
<body>
  <div class="card">
    <svg class="card__backdrop" viewBox="0 0 702 1200" aria-hidden="false">
      <rect class="backdrop__field" x="0" y="0" width="702" height="1200" fill="var(--burgundy)"/>
      <path class="backdrop__sweep"
            d="M0,603 C120,500 330,450 560,438 C600,436 618,420 622,390
               C660,400 680,440 702,505 L702,1200 L0,1200 Z"
            fill="var(--parchment)"/>
      <rect class="backdrop__emblem" role="img"
            aria-label="Broad-lined outline illustration of a dressage horse and rider in mid-stride, drawn in parchment lines"
            x="66" y="28" width="560" height="345" rx="30"
            fill="var(--burgundy-soft)"/>
    </svg>

    <h1 class="card__text card__name">Tod Harlick</h1>
    <p class="card__text card__phone">555-317-0492</p>
    <p class="card__text card__services">
      <span>Classical dressage training</span>
      <span>for the modern American Clinics,</span>
      <span>lessons, training level –</span>
      <span>Prix St. George</span>
    </p>
  </div>
</body>
</html>
```